Land Buying Company Needs Letterhead for Direct Mail Marketing to Land Owners

We are looking for a professional letterhead that we will be including in our direct mail marketing. We will be sending this to land owners who may be interested in selling or purchasing land.

The letterhead needs to be editable. Headers and footers would look nice, but we are open. We would want it to include our address, website, phone, and email info. For right now the address to use for design purposes would the following:

Address: 415 Bramwell Avenue #600
Dallas, TX 75219
Website - www.quillridgeacres.example
Email - info@quillridgeacres.example
Phone - 866-402-ACRE

I have attached our logo zip file that we just had done on Pixel Guild. Let me know what questions you have, and thank you.

```html
<!DOCTYPE html>
<html lang="en">
<head>
<meta charset="utf-8">
<title>Quill Ridge Acres — Letterhead</title>
<link rel="stylesheet" href="https://fonts.googleapis.com/css2?family=Montserrat:wght@700&family=Open+Sans:wght@400&display=swap">
<style>
  :root {
    --forest: #335f00;
    --lime: #8cfc00;
    --paper: #ffffff;
    --mist: #e6ebdf;
  }
  html, body {
    margin: 0;
    padding: 0;
    overflow: hidden;
    background: var(--paper);
  }
  .letterhead {
    position: relative;
    width: 855px;
    height: 1200px;
    overflow: hidden;
    background: var(--paper);
    font-family: "Open Sans", Arial, sans-serif;
  }
  .side-rule {
    position: absolute;
    left: 11px;
    width: 24px;
  }
  .side-rule--dark { top: 11px; height: 857px; background: var(--forest); }
  .side-rule--light { top: 868px; height: 260px; background: var(--lime); }
  .header-band {
    position: absolute;
    left: 11px;
    top: 46px;
    width: 210px;
    height: 118px;
  }
  .brand-dot {
    position: absolute;
    left: 186px;
    top: 56px;
    width: 98px;
    height: 98px;
    border-radius: 50%;
    background: var(--forest);
  }
  .brand-name {
    position: absolute;
    left: 308px;
    top: 58px;
    margin: 0;
    font-family: "Montserrat", Arial, sans-serif;
    font-weight: 700;
    color: var(--lime);
    line-height: 1;
  }
  .brand-name__main {
    display: block;
    font-size: 50px;
    letter-spacing: 1px;
  }
  .brand-name__sub {
    display: block;
    margin-top: 10px;
    font-size: 24px;
    letter-spacing: 17px;
  }
  .contact-row {
    position: absolute;
    top: 208px;
    left: 0;
    width: 855px;
    font-size: 13.5px;
    color: var(--forest);
  }
  .contact-item {
    position: absolute;
    white-space: nowrap;
  }
  .contact-label { color: var(--lime); position: absolute; }
  .contact-item--phone { left: 85px; }
  .contact-item--email { left: 258px; }
  .contact-item--web { left: 532px; }
  .contact-value { position: absolute; left: 26px; }
  .contact-item--web .contact-value { left: 30px; }
  .footer-mark {
    position: absolute;
    left: 201px;
    top: 1078px;
    width: 54px;
    height: 82px;
    background: var(--forest);
  }
  .footer-address {
    position: absolute;
    left: 297px;
    top: 1121px;
    margin: 0;
    font-size: 13.5px;
    color: var(--forest);
    white-space: nowrap;
  }
</style>
</head>
<body>
  <div class="letterhead">
    <div class="side-rule side-rule--dark"></div>
    <div class="side-rule side-rule--light"></div>

    <svg class="header-band" viewBox="0 0 210 118" aria-hidden="true">
      <path d="M0 0 H188 A68 68 0 0 0 192 118 H0 Z" fill="var(--forest)"/>
    </svg>
    <div class="brand-dot" aria-hidden="true"></div>

    <h1 class="brand-name">
      <span class="brand-name__main">QUILL RIDGE</span>
      <span class="brand-name__sub">ACRES</span>
    </h1>

    <div class="contact-row">
      <div class="contact-item contact-item--phone"><span class="contact-label">T:</span><span class="contact-value">866-402-ACRE</span></div>
      <div class="contact-item contact-item--email"><span class="contact-label">E:</span><span class="contact-value">info@quillridgeacres.example</span></div>
      <div class="contact-item contact-item--web"><span class="contact-label">W:</span><span class="contact-value">www.quillridgeacres.example</span></div>
    </div>

    <div class="footer-mark" role="img" aria-label="Small pine tree illustration"></div>
    <p class="footer-address">415 Bramwell Avenue #600 Dallas, TX 75219</p>
  </div>
</body>
</html>
```